Pull-up Banner Design Project

We are a managed account investment company specialising in financial derivatives. Sydney based, our team combines over 100 years of financial markets experience. Our advisers trade the worlds financial markets directly on the clients account whilst the client retains full access and control of the account.
We are holding a seminar in September (and potentially more next year) to showcase our specialist investment program and need to create TWO pull-up banners for the event. The banners need to compliment each other as a Right side, Left side of the stage or presenter, however they should be able to be deployed independently. The size of the banners will be approx 120 cm wide by 200 cm tall.
We have an approved company colour pallet, logos and images. I have provided JPEG versions of these however they can be supplied in Bitmap or GIF if required.
Target Market(s)
Self Managed Superannuation Fund Trustees (Individual Investors)
Industry/Entity Type
Investment
Requirements
Must have
- - Two banner designs - One Right of Stage and one Left of Stage
- Company approved logo
- Company approved colour pallet
- Company approved images
- Can be used independently
- Website: www.quorvenpartners.com.au (can be smallish print)
- Phone: 1300 472 615 (can be smallish print)
Should not have
- Absolutely no images of obscene wealth such as palm trees or speed boats or similar... approved images only.

```html
<!DOCTYPE html>
<html lang="en">
<head>
<meta charset="utf-8">
<title>Quorven Partners – Pull-up Banners</title>
<link href="https://fonts.googleapis.com/css2?family=Ubuntu:wght@300;500;700&display=swap" rel="stylesheet">
<style>
  :root {
    --page-bg: #e4e4e4;
    --banner-white: #ffffff;
    --brand-green: #2b5a41;
    --ink: #1f1f1f;
    --footer-grey: #4b4b4d;
    --footer-text: #ffffff;
    --label-text: #ffffff;
  }
  * { box-sizing: border-box; margin: 0; padding: 0; }
  html, body {
    width: 1200px;
    height: 900px;
    overflow: hidden;
    background: var(--page-bg);
    font-family: "Ubuntu", sans-serif;
  }
  .stage {
    position: relative;
    width: 1200px;
    height: 900px;
  }
  .banner {
    position: absolute;
    top: 56px;
    width: 479px;
    height: 799px;
    display: flex;
    flex-direction: column;
    background: var(--banner-white);
    overflow: hidden;
  }
  .banner--left { left: 61px; }
  .banner--right { left: 639px; }

  .banner__header {
    height: 284px;
    display: flex;
    flex-direction: column;
    align-items: center;
    padding-top: 72px;
  }
  .brand-name {
    font-family: "Ubuntu", sans-serif;
    font-weight: 700;
    font-size: 38px;
    letter-spacing: 0.3px;
    color: var(--brand-green);
    text-transform: uppercase;
    line-height: 1;
    white-space: nowrap;
    max-width: 420px;
  }
  .tagline {
    margin-top: 70px;
    font-weight: 700;
    font-size: 29px;
    line-height: 41px;
    color: var(--ink);
    text-align: center;
    letter-spacing: 0.3px;
  }
  .banner__rule {
    height: 20px;
    background: var(--brand-green);
  }
  .banner__visual {
    position: relative;
    height: 403px;
  }
  .banner__visual--city {
    background:
      linear-gradient(200deg, #dfe8f3 0%, #7f9fcb 22%, #3c5d98 45%, transparent 60%),
      linear-gradient(160deg, #1b2230 0%, #2e3a4f 40%, #151a23 100%);
  }
  .banner__visual--stones {
    background:
      radial-gradient(ellipse at 30% 30%, #4a4d45 0%, transparent 55%),
      radial-gradient(ellipse at 70% 75%, #3f443a 0%, transparent 50%),
      linear-gradient(180deg, #2a2c29 0%, #1e201d 100%);
  }
  .visual__label {
    position: absolute;
    top: 42px;
    right: 52px;
    font-weight: 300;
    font-size: 35px;
    color: var(--label-text);
    letter-spacing: 0.3px;
  }
  .banner--right .visual__label { right: 24px; }
  .banner__footer {
    flex: 1;
    background: var(--footer-grey);
    color: var(--footer-text);
    display: flex;
    flex-direction: column;
    align-items: center;
    justify-content: center;
    font-weight: 700;
    font-size: 22px;
    line-height: 32px;
    letter-spacing: 0.3px;
  }
</style>
</head>
<body>
<main class="stage">

  <section class="banner banner--left" aria-label="Left of stage banner">
    <header class="banner__header">
      <div class="brand-name">Quorven Partners</div>
      <p class="tagline">Australian owned<br>Real results</p>
    </header>
    <div class="banner__rule"></div>
    <div class="banner__visual banner__visual--city" role="img" aria-label="Photo looking up at glass office towers against a blue sky with clouds">
      <span class="visual__label">Professional</span>
    </div>
    <footer class="banner__footer">
      <span>www.quorvenpartners.com.au</span>
      <span>Phone: 1300 472 615</span>
    </footer>
  </section>

  <section class="banner banner--right" aria-label="Right of stage banner">
    <header class="banner__header">
      <div class="brand-name">Quorven Partners</div>
      <p class="tagline">Australian owned<br>Real results</p>
    </header>
    <div class="banner__rule"></div>
    <div class="banner__visual banner__visual--stones" role="img" aria-label="Photo of polished dark green jade pebbles piled together">
      <span class="visual__label">Collaborative</span>
    </div>
    <footer class="banner__footer">
      <span>www.quorvenpartners.com.au</span>
      <span>Phone: 1300 472 615</span>
    </footer>
  </section>

</main>
</body>
</html>
```